VARNOLA SYSTEMS BUSINESS CARD DESIGN

WE WANT COMPLETE NEW DESIGN OF OUR BUSINESS CARD. WE ARE AN INTEGRATION COMPANY, WHERE WE INTEGRATE IOT/SMART SYSTEMS TO HOMES AND CORPORATE CUSTOMERS. WE SUPPLY AND INSTALL AUTOMATION PRODUCTS. THE FINAL DESIGN SHOULD COMMUNICATE TECHNOLOGY. THE CARD DESIGN SHOULD BE VERY IMPACT FULL. LOGO NEEDS TO BE THERE. IT WOULD NICE IF THE DESIGN WAS CLEAN. COLORS IS UP TO DESIGNER TO PLAY WITH, OR CAN STICK TO CORPORATE COLORS (FOLLOW LOGO). I HAVE ADDED FEW REFERENCE PHOTOS TO DRAW INSPIRATION MAYBE. I HAVE ADDED A HEX DESIGN, ITS NOT NECESSARY TO USE THIS DESIGN, ITS UPTO DESIGNER, JUST ADDED IF NEEDED TO PLAY WITH DESIGN.

Target Market(s)

Private end users and corporate clients

Industry/Entity Type

technology, home automation, home theaters, building management systems, IOT

Contact Information for Business Card

It should include Employee name, personal number, office number, email address, both in English and arabic. DETAILS TO INCLUDE :GERALD MOSSANE, MOBILE 0097150738915,OFFCIE 009714386207, GERALD@VARNOLAHUB.CO

Requirements
Must have
• Should feel like a technology company from design. Details both and in English and arabic (or at least have provision for arabic in design).
Nice to have
• I would like logo on one side, and details on the other side. Logo design side should communicate technology with logo. Other side can be clean just with information or also have some design aspects following from logo side. it would be interesting to see submissions with square design as well (that looks like an app Icon). colors could be of logo, red black grey and white. I have added some designs to draw inspiration from

```html
<!DOCTYPE html>
<html lang="en">
<head>
<meta charset="utf-8">
<title>Varnola Systems Business Card</title>
<link rel="stylesheet" href="https://fonts.googleapis.com/css2?family=Questrial&display=swap">
<style>
  :root {
    --stage: #e4e4e4;
    --ink: #111111;
    --card-black: #070707;
    --paper: #f7f7f7;
    --red: #ee1c25;
    --red-soft: #f7c6c8;
    --grey: #a9a9a9;
    --grey-dark: #5a5a5a;
    --white: #ffffff;
  }
  * { box-sizing: border-box; margin: 0; padding: 0; }
  html, body {
    width: 1200px; height: 800px; overflow: hidden;
    background: var(--stage);
    font-family: "Questrial", sans-serif;
    color: var(--ink);
  }
  .canvas {
    position: relative; width: 1200px; height: 800px;
    display: flex; align-items: center; justify-content: center; gap: 40px;
  }
  .card {
    position: relative; width: 540px; height: 320px; overflow: hidden;
  }
  /* Logo side */
  .card--back { background: var(--card-black); }
  .back-mark {
    position: absolute; left: 0; right: 0; top: 110px;
    display: flex; align-items: center; justify-content: center; gap: 18px;
  }
  .mark-dot {
    width: 58px; height: 58px; border-radius: 50%; background: var(--red);
  }
  .brand-name--back {
    font-size: 40px; letter-spacing: 3px; color: var(--white);
  }
  .web-address {
    position: absolute; right: 30px; bottom: 26px;
    font-size: 15px; letter-spacing: 5px; color: var(--white);
  }
  /* Details side */
  .card--front {
    background: linear-gradient(170deg, var(--red-soft) 0%, #f36a70 55%, var(--red) 100%);
  }
  .front-panel {
    position: absolute; inset: 14px; background: var(--paper);
  }
  .brand-lockup {
    position: absolute; left: 26px; top: 22px;
    display: flex; align-items: center; gap: 10px;
  }
  .brand-dot { width: 26px; height: 26px; border-radius: 50%; background: var(--red); }
  .brand-name--front { font-size: 26px; letter-spacing: 1px; color: var(--ink); }
  .division {
    position: absolute; left: 28px; top: 62px;
    font-size: 10px; letter-spacing: 3px; color: var(--ink);
  }
  .person-name {
    position: absolute; left: 28px; top: 96px;
    font-size: 21px; color: var(--ink);
  }
  .contact-list {
    position: absolute; left: 28px; top: 136px;
    list-style: none; font-size: 12.5px; line-height: 1.45; color: var(--ink);
  }
  .front-deco {
    position: absolute; right: 24px; bottom: 22px;
    display: flex; align-items: center; gap: 12px;
  }
  .deco-dot { width: 70px; height: 70px; border-radius: 50%; background: var(--red); }
  .deco-name { font-size: 30px; letter-spacing: 2px; color: var(--grey-dark); }
</style>
</head>
<body>
  <main class="canvas">
    <section class="card card--back" aria-label="Business card, logo side">
      <div class="back-mark">
        <span class="mark-dot"></span>
        <span class="brand-name--back">VARNOLA</span>
      </div>
      <p class="web-address">varnolahub.co</p>
    </section>

    <section class="card card--front" aria-label="Business card, details side">
      <div class="front-panel">
        <div class="brand-lockup">
          <span class="brand-dot"></span>
          <span class="brand-name--front">VARNOLA SYSTEMS</span>
        </div>
        <p class="division">A VARNOLA GROUP DIVISION.</p>
        <h1 class="person-name">Gerald Mossane</h1>
        <ul class="contact-list">
          <li>Mobile 0097150738915</li>
          <li>Office 009714386207</li>
          <li>Gerald@varnolahub.co</li>
        </ul>
        <div class="front-deco">
          <span class="deco-dot"></span>
          <span class="deco-name">VARNOLA</span>
        </div>
      </div>
    </section>
  </main>
</body>
</html>
```